French for French

Cover for the book "The Plume Vagabonde" ("How to write in French"). The book seeks to teach English to English: words, grammar, syntax. The lessons are pleasant, the style is very classical.

Target Market(s)

Middle class interested in improving her language.

Industry/Entity Type

Publishing Company

Colors

Designer to choose colors to be used in the design.

Requirements
Must have
• Author: "Marcel Tournevin" Title: "The Roving Quill" Publisher: "Corvane Editions" Size: 14 x 20,5 cm

```html
<!DOCTYPE html>
<html lang="en">
<head>
<meta charset="utf-8">
<title>The Roving Quill — Marcel Tournevin</title>
<link rel="stylesheet" href="https://fonts.googleapis.com/css2?family=Jost:wght@200;300&family=Oswald:wght@500;600&family=Cormorant+Garamond:wght@500&display=swap">
<style>
  :root {
    --ink: #050505;
    --paper: #ffffff;
    --soft: #d9d6cf;
    --glow: #f3ead6;
    --glow-mid: #6b6459;
  }
  html, body {
    margin: 0;
    padding: 0;
    width: 820px;
    height: 1200px;
    overflow: hidden;
    background: var(--ink);
  }
  .cover {
    position: relative;
    width: 820px;
    height: 1200px;
    background: var(--ink);
    color: var(--paper);
    overflow: hidden;
  }
  .cover-art {
    position: absolute;
    left: 0;
    top: 380px;
    width: 820px;
    height: 690px;
    background:
      radial-gradient(ellipse 300px 90px at 50% 86%, var(--glow) 0%, rgba(243,234,214,0.55) 35%, rgba(0,0,0,0) 75%),
      radial-gradient(ellipse 420px 320px at 50% 45%, rgba(107,100,89,0.45) 0%, rgba(5,5,5,0) 70%),
      var(--ink);
  }
  .title {
    position: absolute;
    left: 0;
    top: 110px;
    width: 820px;
    height: 300px;
    margin: 0;
    font-weight: normal;
    text-transform: uppercase;
    line-height: 1;
  }
  .title-line {
    position: absolute;
    display: block;
    white-space: nowrap;
  }
  .thin {
    font-family: "Jost", "Helvetica Neue", sans-serif;
    font-weight: 200;
  }
  .bold {
    font-family: "Oswald", "Arial Narrow", sans-serif;
    font-weight: 600;
  }
  .line-one {
    left: 108px;
    top: 0;
  }
  .line-one .big { font-size: 100px; letter-spacing: 1px; }
  .line-one .small { font-size: 72px; margin-left: 18px; }
  .line-two {
    left: 300px;
    top: 110px;
    font-size: 150px;
    letter-spacing: 2px;
  }
  .subtitle {
    position: absolute;
    left: 0;
    top: 648px;
    width: 820px;
    text-align: center;
    margin: 0;
    font-family: "Cormorant Garamond", Georgia, serif;
    font-weight: 500;
    font-size: 27px;
    letter-spacing: 1px;
    color: var(--soft);
  }
  .subtitle .joiner {
    font-size: 18px;
    text-transform: lowercase;
  }
  .author {
    position: absolute;
    left: 0;
    top: 1072px;
    width: 820px;
    text-align: center;
    margin: 0;
    font-family: "Oswald", "Arial Narrow", sans-serif;
    font-weight: 500;
    font-size: 54px;
    line-height: 1.2;
    letter-spacing: 2px;
    text-transform: uppercase;
  }
  .publisher {
    position: absolute;
    left: 0;
    top: 1146px;
    width: 820px;
    text-align: center;
    margin: 0;
    font-family: "Cormorant Garamond", Georgia, serif;
    font-weight: 500;
    font-size: 20px;
    letter-spacing: 6px;
    text-transform: uppercase;
    color: var(--soft);
  }
</style>
</head>
<body>
  <main class="cover">
    <div class="cover-art" role="img" aria-label="An open book glowing with light, with letters of the alphabet flying up from its pages into the dark"></div>

    <h1 class="title">
      <span class="title-line line-one"><span class="thin big">The</span><span class="thin small">Roving</span></span>
      <span class="title-line line-two bold">Quill</span>
    </h1>

    <p class="subtitle">FRENCH <span class="joiner">to</span> FRENCH</p>

    <p class="author">Marcel Tournevin</p>
    <p class="publisher">Editions Corvane</p>
  </main>
</body>
</html>
```